NEW Modern Sleek Business Card for VR Language Startup

Our startup is using VR to lead the next wave of world language education. We need a two-sided business card that introduces the larger organization (Quorvel Language Inc) and our contact info on one side and shows the product, Lumidrasca, on the other side.

Side 1 (contact info)= Quorvel Logo and Contact info (name, title, phone, email)

Side 2 (product)= Lumidrasc logo, text, and website
Text= Culturally Immersive Language Learning Games
Website= www.lumidrasc.example

Target Market(s)

Education, Technology

Contact Information for Business Card

Contact info will be updated upon approval of the design. For now, put this as a placeholder.

Perry Hollins
Founder & CEO
phollins@mailtrove.example
(555)-014-2736

Font styles to use
Other font styles liked:
• Gibson and Century Gothic are the brand fonts

Requirements
Nice to have
• I would love to see cohesion between the design and colors of the two logos. I have attached a few business card designs that I like, so you can get a feel for my preferred style.

```html
<!DOCTYPE html>
<html lang="en">
<head>
<meta charset="utf-8">
<title>Quorvel Language – Business Card</title>
<link href="https://fonts.googleapis.com/css2?family=Questrial&family=Montserrat:wght@600&display=swap" rel="stylesheet">
<style>
  :root {
    --page: #ffffff;
    --heading: #1a3cf0;
    --rule: #111111;
    --navy-deep: #0b1230;
    --navy: #15215a;
    --navy-glow: #2a4bb0;
    --navy-back: #141a36;
    --white: #ffffff;
    --teal: #3aa7a3;
    --teal-text: #5fc4d0;
    --dot: #4a5cb8;
    --divider: #3b4aa8;
    --text-soft: #e6e8f2;
    --product-grey: #5a6b8c;
  }
  * { box-sizing: border-box; margin: 0; padding: 0; }
  html, body { width: 818px; height: 1200px; overflow: hidden; background: var(--page); }
  body { position: relative; font-family: "Questrial", "Century Gothic", sans-serif; }

  .sheet-title {
    position: absolute; left: 0; right: 0; top: 66px;
    font-family: "Questrial", sans-serif; font-size: 29px; font-weight: 400; line-height: 1.2;
    color: var(--heading); text-align: center; white-space: nowrap;
  }
  .sheet-rule {
    position: absolute; left: 36px; top: 107px; width: 748px; height: 3px;
    background: var(--rule); border-radius: 2px;
  }

  .card { position: absolute; overflow: hidden; }

  /* Front */
  .card-front { left: 24px; top: 230px; width: 772px; height: 441px; background: var(--navy-deep); }
  .front-backdrop {
    position: absolute; inset: 0;
    background:
      radial-gradient(ellipse 60% 80% at 18% 35%, var(--navy-glow) 0%, rgba(42,75,176,0.35) 45%, transparent 75%),
      radial-gradient(ellipse 50% 60% at 55% 25%, rgba(40,70,170,0.45) 0%, transparent 70%),
      linear-gradient(110deg, var(--navy) 0%, var(--navy-deep) 70%);
  }
  .brand-mark {
    position: absolute; left: 40px; top: 150px; display: flex; align-items: center; gap: 14px;
  }
  .brand-mark .brand-dot { width: 34px; height: 34px; border-radius: 50%; background: var(--white); }
  .brand-mark .brand-name {
    font-family: "Questrial", sans-serif; font-size: 52px; color: var(--white); letter-spacing: 3px;
  }

  .contact-name {
    position: absolute; right: 36px; top: 40px;
    font-family: "Montserrat", sans-serif; font-weight: 600; font-size: 54px;
    color: var(--white); letter-spacing: -0.5px; line-height: 1;
  }
  .contact-title {
    position: absolute; right: 132px; top: 99px;
    font-size: 20px; color: var(--teal-text); letter-spacing: 0.5px;
  }
  .contact-list { position: absolute; right: 46px; top: 184px; list-style: none; }
  .contact-item {
    display: flex; align-items: center; justify-content: flex-end; gap: 12px;
    height: 40px; margin-bottom: 36px;
    font-size: 24px; color: var(--white);
  }
  .contact-icon {
    width: 40px; height: 40px; border-radius: 50%; background: var(--teal);
    display: flex; align-items: center; justify-content: center; flex: none;
  }

  /* Back */
  .card-back { left: 22px; top: 720px; width: 776px; height: 443px; background: var(--navy-back); }
  .back-backdrop {
    position: absolute; inset: 0;
    background:
      radial-gradient(ellipse 45% 70% at 48% 40%, rgba(30,40,85,0.8) 0%, transparent 75%),
      linear-gradient(180deg, #131a35 0%, #121834 100%);
  }
  .product-mark {
    position: absolute; left: 0; right: 0; top: 170px;
    display: flex; justify-content: center; align-items: center; gap: 14px;
  }
  .product-mark .product-dot { width: 30px; height: 30px; border-radius: 50%; background: var(--product-grey); }
  .product-mark .product-name {
    font-family: "Questrial", sans-serif; font-size: 46px; line-height: 1; color: var(--product-grey);
  }

  .feature-col { position: absolute; top: 240px; list-style: none; }
  .feature-col li {
    display: flex; align-items: center; gap: 8px; height: 26px; margin-bottom: 20px;
    font-size: 19px; color: var(--text-soft); letter-spacing: 0.3px; white-space: nowrap;
  }
  .feature-left li::before, .feature-right li::after {
    content: ""; width: 22px; height: 22px; border-radius: 50%; background: var(--dot); flex: none;
  }
  .feature-left { left: 96px; }
  .feature-right { right: 110px; text-align: right; }
  .feature-right li { justify-content: flex-end; }
  .feature-divider {
    position: absolute; left: 382px; top: 244px; width: 1px; height: 113px; background: var(--divider);
  }
  .product-site {
    position: absolute; left: 0; right: 0; top: 384px; text-align: center;
    font-size: 22px; color: var(--text-soft); letter-spacing: 1.5px;
  }
</style>
</head>
<body>
  <h1 class="sheet-title">New Modern Sleek Business Card for VR Laguage Startup</h1>
  <div class="sheet-rule"></div>

  <section class="card card-front">
    <div class="front-backdrop" role="img" aria-label="Deep blue backdrop with glowing bokeh lights and a faint hexagonal network pattern"></div>
    <div class="brand-mark">
      <span class="brand-dot"></span>
      <span class="brand-name">Quorvel</span>
    </div>

    <h2 class="contact-name">Perry Hollins</h2>
    <p class="contact-title">Founder &amp; CEO</p>

    <ul class="contact-list">
      <li class="contact-item">
        <span>(555)-014-2736</span>
        <span class="contact-icon">
          <svg width="22" height="22" viewBox="0 0 24 24"><path fill="#fff" d="M6.6 10.8a15.1 15.1 0 0 0 6.6 6.6l2.2-2.2c.3-.3.7-.4 1-.2 1.1.4 2.3.6 3.6.6.6 0 1 .4 1 1V20c0 .6-.4 1-1 1A17 17 0 0 1 3 4c0-.6.4-1 1-1h3.5c.6 0 1 .4 1 1 0 1.3.2 2.5.6 3.6.1.3 0 .7-.2 1z"/></svg>
        </span>
      </li>
      <li class="contact-item">
        <span>phollins@mailtrove.example</span>
        <span class="contact-icon">
          <svg width="22" height="16" viewBox="0 0 22 16"><rect x="1" y="1" width="20" height="14" rx="1" fill="#fff"/><path d="M1.5 1.5 11 9l9.5-7.5M1.5 14.5 8 8.5M20.5 14.5 14 8.5" stroke="#3aa7a3" stroke-width="1.3" fill="none"/></svg>
        </span>
      </li>
      <li class="contact-item">
        <span>Marlow, Fenwick Lane, Nr 12</span>
        <span class="contact-icon">
          <svg width="22" height="20" viewBox="0 0 22 20"><path fill="#fff" d="M11 1 1 10h3v9h5v-6h4v6h5v-9h3z"/></svg>
        </span>
      </li>
    </ul>
  </section>

  <section class="card card-back">
    <div class="back-backdrop" role="img" aria-label="Dark navy backdrop with a faint large decorative shape"></div>
    <div class="product-mark">
      <span class="product-dot"></span>
      <span class="product-name">Lumidrasc</span>
    </div>

    <ul class="feature-col feature-left">
      <li>Attain Proficiency</li>
      <li>Maintain proficiency</li>
      <li>Total Immersion</li>
    </ul>
    <div class="feature-divider"></div>
    <ul class="feature-col feature-right">
      <li>Game-based Learning</li>
      <li>Build Cultural Awareness</li>
      <li>Highest Learning Transfer</li>
    </ul>

    <p class="product-site">www.lumidrasc.example</p>
  </section>
</body>
</html>
```